Sofware box design

We need a design for the software box for Chinese language e-learning course series. The box should contain such an elements:
- Software title and subtitle: Qiaobu! Chinese e-learning course for beginners
- The separated information about the course series: The innovative e-learning series
- The separated information about the difficulty level of the course: A1 - Beginner.
We want to get a clear form design which should communicate for potential customers information as following:
- online
- innovative
- helpful
- user friendly
- effective
Software

```html
<!DOCTYPE html>
<html lang="en">
<head>
<meta charset="utf-8">
<title>Qiaobu! Chinese e-learning course for beginners</title>
<link rel="stylesheet" href="https://fonts.googleapis.com/css2?family=Arimo:wght@700&family=Yuji+Boku&display=swap">
<style>
  :root {
    --backdrop: #ececec;
    --paper: #f2f0ea;
    --scene-light: #e9e7e0;
    --scene-mid: #c9c8c0;
    --red: #c8202a;
    --red-dark: #7a1a1c;
    --ink: #111111;
    --white: #ffffff;
  }
  * { margin: 0; padding: 0; box-sizing: border-box; }
  html, body {
    width: 1200px; height: 864px; overflow: hidden;
    background: var(--backdrop);
  }
  .box-layout {
    position: absolute; left: 280px; top: 92px;
    width: 640px; height: 680px;
    display: flex;
  }
  .spine { width: 140px; height: 680px; }
  .front {
    position: relative; width: 500px; height: 680px;
    background: var(--paper); overflow: hidden;
  }
  .front-art { position: absolute; inset: 0; }
  .landscape-illustration {
    position: absolute; left: 0; top: 120px; width: 500px; height: 460px;
    background: radial-gradient(ellipse at 40% 55%, var(--scene-mid) 0%, var(--scene-light) 55%, var(--paper) 100%);
  }
  .series-label, .level-label, .subtitle {
    font-family: "Arimo", Arial, sans-serif; font-weight: 700;
  }
  .title-mark {
    position: absolute; left: 48px; top: 262px;
    font-family: "Yuji Boku", serif; font-size: 92px; line-height: 1;
    font-weight: 400; color: var(--ink);
  }
  .subtitle {
    position: absolute; left: 72px; top: 580px;
    font-size: 30px; line-height: 1.25; color: var(--ink);
  }
</style>
</head>
<body>
<main class="box-layout">
  <svg class="spine" viewBox="0 0 140 680" aria-label="Box spine">
    <defs>
      <linearGradient id="spine-red" x1="0" x2="1" y1="0" y2="0">
        <stop offset="0" stop-color="#9e1c20"/>
        <stop offset="1" stop-color="#d32a2f"/>
      </linearGradient>
    </defs>
    <rect width="140" height="680" fill="url(#spine-red)"/>
    <path d="M0 0 H70 Q20 200 0 420 Z" fill="var(--red-dark)" opacity="0.7"/>
    <text transform="translate(30 30) rotate(90)" font-family="Arimo, Arial, sans-serif" font-weight="700" font-size="26" fill="var(--white)">Chinese e-learning</text>
    <text transform="translate(62 360) rotate(90)" font-family="'Yuji Boku', serif" font-size="60" fill="var(--white)">Qiaobu!</text>
    <text transform="translate(52 628) rotate(90)" font-family="Arimo, Arial, sans-serif" font-weight="700" font-size="36" fill="var(--white)">A1</text>
  </svg>

  <section class="front">
    <div class="landscape-illustration" role="img" aria-label="Traditional Chinese ink landscape with willow tree, pavilion and boat on a river"></div>
    <svg class="front-art" viewBox="0 0 500 680">
      <defs>
        <linearGradient id="corner-red" x1="0" x2="1" y1="0" y2="0">
          <stop offset="0" stop-color="#a81c22"/>
          <stop offset="1" stop-color="var(--red)"/>
        </linearGradient>
        <path id="series-curve" d="M14 34 Q470 52 468 480"/>
      </defs>
      <path d="M20 0 H500 V470 Q500 20 20 0 Z" fill="url(#corner-red)"/>
      <text class="series-label" font-size="24" fill="var(--ink)">
        <textPath href="#series-curve">The innovative e-learning series</textPath>
      </text>
      <text class="level-label" x="485" y="90" text-anchor="end" font-size="30" fill="var(--white)">BEGINNER</text>
      <text class="level-label" x="485" y="160" text-anchor="end" font-size="60" fill="var(--white)">A1</text>
    </svg>
    <h1 class="title-mark">Qiaobu!</h1>
    <p class="subtitle">Chinese e-learning<br>course for beginners</p>
  </section>
</main>
</body>
</html>
```